VANTA SWEEP

Need a professional looking business card that can fit : Name, Title, Cell, and office phone numbers. On the flip side we would like a list of our services : Highway accident management and towing, Crime scene clean up, Illegal drug lab clean up, Drug disposal, and Hazardous materials clean up.

```html
<!DOCTYPE html>
<html lang="en">
<head>
<meta charset="utf-8">
<title>Vanta Sweep — Business Card</title>
<link rel="stylesheet" href="https://fonts.googleapis.com/css2?family=Cinzel:wght@400;600;700&display=swap">
<style>
  :root {
    --navy: #1d3a5e;
    --gold: #d6a21e;
    --red: #c41f30;
    --paper: #f7f7f5;
    --ground: #e8e5e1;
    --white: #ffffff;
  }
  * { box-sizing: border-box; margin: 0; padding: 0; }
  html, body {
    width: 1200px; height: 1200px; overflow: hidden;
    background: var(--ground);
    font-family: "Cinzel", "Times New Roman", serif;
    color: var(--navy);
  }
  .sheet {
    width: 1200px; height: 1200px;
    display: flex; flex-direction: column; align-items: center;
    justify-content: center; gap: 26px;
  }
  .card {
    position: relative;
    width: 960px; height: 549px;
    background: var(--paper);
    box-shadow: 0 6px 18px rgba(0,0,0,0.18);
    overflow: hidden;
  }
  /* front */
  .band {
    position: absolute; left: 0; right: 0; top: 150px; height: 118px;
    background: var(--navy);
  }
  .brand {
    position: absolute; left: 56px; top: 140px; height: 138px;
    padding: 0 22px;
    display: flex; align-items: center; gap: 16px;
    background: var(--paper);
    white-space: nowrap;
  }
  .brand-dot {
    width: 52px; height: 52px; border-radius: 50%;
    background: var(--navy); flex: none;
  }
  .brand-name {
    font-weight: 700; font-size: 32px; letter-spacing: 1px;
    color: var(--navy);
  }
  .identity {
    position: absolute; right: 60px; top: 168px; text-align: right;
    white-space: nowrap;
  }
  .person-name {
    color: var(--white); font-weight: 700; font-size: 38px; line-height: 1.1;
  }
  .person-title {
    color: var(--gold); font-weight: 400; font-size: 28px; margin-top: 4px;
  }
  .contact {
    position: absolute; right: 60px; top: 300px; text-align: right;
    font-size: 28px; line-height: 1.35; white-space: nowrap;
  }
  .contact-row {
    display: flex; justify-content: flex-end; align-items: center; gap: 30px;
  }
  .contact-item { display: inline-flex; align-items: center; gap: 10px; }
  .icon { width: 28px; height: 28px; fill: var(--navy); flex: none; }
  /* back */
  .services {
    position: absolute; left: 62px; top: 168px;
    list-style: none; font-size: 31px; line-height: 1.28;
  }
  .services li { display: flex; align-items: center; gap: 10px; white-space: nowrap; }
  .star { width: 24px; height: 24px; fill: var(--red); flex: none; }
</style>
</head>
<body>
<main class="sheet">

  <section class="card card-front">
    <div class="band"></div>
    <div class="brand">
      <span class="brand-dot"></span>
      <span class="brand-name">VANTA SWEEP</span>
    </div>
    <div class="identity">
      <div class="person-name">Harold J Benton</div>
      <div class="person-title">Principal</div>
    </div>
    <div class="contact">
      <div>2417 Cedar Hollow Road</div>
      <div>Riverton, WV 25407</div>
      <div class="contact-row">
        <span class="contact-item">
          <svg class="icon" viewBox="0 0 24 24"><rect x="6" y="1" width="12" height="22" rx="2"/><rect x="8" y="4" width="8" height="13" fill="#f7f7f5"/><circle cx="12" cy="20" r="1.2" fill="#f7f7f5"/></svg>
          (304) 555-0142
        </span>
        <span class="contact-item">
          <svg class="icon" viewBox="0 0 24 24"><rect x="2" y="3" width="6" height="18" rx="2"/><rect x="9" y="5" width="13" height="16" rx="1.5"/><rect x="11" y="7" width="9" height="4" fill="#f7f7f5"/><g fill="#f7f7f5"><rect x="11" y="13" width="2" height="2"/><rect x="14.5" y="13" width="2" height="2"/><rect x="18" y="13" width="2" height="2"/><rect x="11" y="16.5" width="2" height="2"/><rect x="14.5" y="16.5" width="2" height="2"/><rect x="18" y="16.5" width="2" height="2"/></g></svg>
          (304) 555-0178
        </span>
      </div>
      <div class="contact-row">
        <span class="contact-item">
          <svg class="icon" viewBox="0 0 24 24"><rect x="1" y="5" width="22" height="15" rx="1"/><path d="M2 6 L12 14 L22 6" fill="none" stroke="#f7f7f5" stroke-width="1.6"/></svg>
          info@vantasweep.com
        </span>
      </div>
    </div>
  </section>

  <section class="card card-back">
    <ul class="services">
      <li><svg class="star" viewBox="0 0 24 24"><path d="M12 1.5l3.1 7 7.4.6-5.6 4.9 1.7 7.3L12 17.4 5.4 21.3l1.7-7.3L1.5 9.1l7.4-.6z"/></svg>Highway accident management and towing</li>
      <li><svg class="star" viewBox="0 0 24 24"><path d="M12 1.5l3.1 7 7.4.6-5.6 4.9 1.7 7.3L12 17.4 5.4 21.3l1.7-7.3L1.5 9.1l7.4-.6z"/></svg>Crime scene clean up</li>
      <li><svg class="star" viewBox="0 0 24 24"><path d="M12 1.5l3.1 7 7.4.6-5.6 4.9 1.7 7.3L12 17.4 5.4 21.3l1.7-7.3L1.5 9.1l7.4-.6z"/></svg>Illegal drug lab clean up</li>
      <li><svg class="star" viewBox="0 0 24 24"><path d="M12 1.5l3.1 7 7.4.6-5.6 4.9 1.7 7.3L12 17.4 5.4 21.3l1.7-7.3L1.5 9.1l7.4-.6z"/></svg>Drug disposal and</li>
      <li><svg class="star" viewBox="0 0 24 24"><path d="M12 1.5l3.1 7 7.4.6-5.6 4.9 1.7 7.3L12 17.4 5.4 21.3l1.7-7.3L1.5 9.1l7.4-.6z"/></svg>Hazardous materials clean up</li>
    </ul>
  </section>

</main>
</body>
</html>
```